Brantley Advisory Group provides support for renewable energy projects to utilities and suppliers

I need a professional looking business card that is both simple and elegant and unique. My clients are mostly large organizations not individuals. I am a consultant with my own company that is small but would like to give clients the impression I am larger. Smart grid, fiber optics, software, field hardware, distribution automation, substation automation, operations, energy storage/batteries, microgrids, customer service, strategy/roadmaps, conservation, Automated Metering Infrastruture (AMI or smart meters) are all areas of focus.

Target Market(s)

Utilities, suppliers, governmental agencies involved in energy. All types of energy especially natural gas and electrical. Especially renewable energy or green projects.

Contact Information for Business Card

Name - Mark Brantley Cell Phone - 425.318.2746 Email - mbrantley@brantleyag-example.com
Company - Brantley Advisory Group (logo) Title - Principal

Font styles to use
Serif
Sans Serif

Colors

Designer to choose colors to be used in the design.

Requirements
Must have
• Simple and professional and powerful.
• Unique/creative design.
Nice to have
• Utilize color scheme to accent logo colors. Maybe some geometric pattern on edge of card with color.
Should not have
• Busy, complicated, traditional

```html
<!DOCTYPE html>
<html lang="en">
<head>
<meta charset="utf-8">
<title>Brantley Advisory Group — Business Card</title>
<link href="https://fonts.googleapis.com/css2?family=Montserrat:wght@400;500;600&display=swap" rel="stylesheet">
<style>
  :root {
    --backdrop: #b5b5b5;
    --paper: #f7f7f7;
    --navy: #1a3a94;
    --royal: #1b3a8f;
    --royal-deep: #16307a;
    --leaf: #4d8a2a;
    --ink: #444444;
  }
  * { margin: 0; padding: 0; box-sizing: border-box; }
  html, body {
    width: 1200px; height: 750px; overflow: hidden;
    background: var(--backdrop);
    font-family: "Montserrat", sans-serif;
  }
  .stage { position: relative; width: 1200px; height: 750px; }
  .card {
    position: absolute; top: 226px;
    width: 502px; height: 286px;
    border-radius: 14px; overflow: hidden;
  }
  .card--front { left: 90px; background: var(--paper); }
  .card--back { left: 612px; background: var(--royal); }

  .brand {
    position: absolute; left: 37px; top: 46px;
    display: flex; align-items: center; gap: 10px;
  }
  .brand__mark { width: 26px; height: 26px; background: var(--navy); }
  .brand__name {
    font-weight: 600; font-size: 20px; color: var(--navy);
    line-height: 1.05; width: 170px;
  }
  .rule {
    position: absolute; left: 37px; top: 163px;
    width: 18px; height: 2px; background: var(--navy);
  }
  .person__name {
    position: absolute; left: 37px; top: 178px;
    font-size: 16px; font-weight: 500; color: var(--navy);
  }
  .person__title {
    position: absolute; left: 36px; top: 199px;
    font-size: 13px; color: var(--leaf);
  }
  .contact {
    position: absolute; left: 37px; top: 227px;
    font-size: 10.5px; color: var(--ink); line-height: 15px;
  }
  .website {
    position: absolute; right: 30px; top: 242px;
    font-size: 10.5px; font-weight: 500; color: var(--ink);
    letter-spacing: 1.4px;
  }

  .back-brand {
    position: absolute; left: 0; right: 0; top: 0; bottom: 0;
    display: flex; align-items: center; justify-content: center; gap: 14px;
  }
  .back-brand__mark { width: 46px; height: 46px; border: 3px solid var(--royal-deep); }
  .back-brand__name {
    font-weight: 600; font-size: 30px; color: var(--royal-deep);
    line-height: 1.1; width: 230px;
  }
</style>
</head>
<body>
<main class="stage">
  <section class="card card--front" aria-label="Card front">
    <div class="brand">
      <span class="brand__mark"></span>
      <span class="brand__name">Brantley Advisory Group</span>
    </div>
    <div class="rule"></div>
    <p class="person__name">Mark Brantley Cell</p>
    <p class="person__title">Principal</p>
    <p class="contact">425.318.2746<br>mbrantley@brantleyag-example.com</p>
    <p class="website">www.brantleyag-example.com</p>
  </section>

  <section class="card card--back" aria-label="Card back">
    <div class="back-brand">
      <span class="back-brand__mark"></span>
      <span class="back-brand__name">Brantley Advisory Group</span>
    </div>
  </section>
</main>
</body>
</html>
```